Business Cards and Logo

KMR - Personal Injury Attorneys is the name of the firm.
We are personal injury lawyers. We want a crisp, modern and impactful design.
Color schemes are white, matte black and light grey OR white, matte black and red OR white, matte black and a nice blue or yellow.
For logo - we don’t want typical logos like scales of justice or a hammer. We want a general design with the KMR letters.
Target Market(s)
People who need attorneys.
Industry/Entity Type
Law Firm
Contact Information for Business Card
Back side: text: Port Alder - Cedar Vale - Marisol Bay - North Hollis
Front side
Name of firm and logo.
Tobin Verulakis
812 W. Holloway Ave. 4th Floor
Larkhaven, CA 90412
(555)471-6029 (c)
(555)963-1157 (o)
Tobin@counselwestmail.example
Logo Text
KMR
Font styles to use
Other font styles liked:
- Musk - regular. Military - regular. Moonglade. Future. Or similar fonts.
Requirements
Must have
- See above. Nothing else to provide.
- KMR - Personal Injury Attorneys is the name of the firm.
- We are personal injury lawyers. We want a crisp, modern and impactful design.
- Color schemes are white, matte black and light grey OR white, matte black and red OR white, matte black and a nice blue or yellow.
- For logo - we don’t want typical logos like scales of justice or a hammer. We want a general design with the KMR letters.
Nice to have
- See above - nothing else to provide.
Should not have

```html
<!DOCTYPE html>
<html lang="en">
<head>
<meta charset="utf-8">
<title>KMR Personal Injury Attorneys – Business Card</title>
<link rel="stylesheet" href="https://fonts.googleapis.com/css2?family=EB+Garamond:wght@400;500&display=swap">
<style>
  :root {
    --backdrop: #1d1d1f;
    --brand-blue: #2a76b8;
    --card-white: #ffffff;
    --steel-grey: #8e8e8e;
    --ink: #4a4a4a;
  }
  * { margin: 0; padding: 0; box-sizing: border-box; }
  html, body { width: 1200px; height: 895px; overflow: hidden; }
  body {
    background: var(--backdrop);
    font-family: "EB Garamond", "Times New Roman", serif;
    font-variant: small-caps;
    position: relative;
  }
  .card {
    position: absolute;
    width: 540px;
    height: 309px;
    box-shadow: 0 14px 30px rgba(0,0,0,.55);
  }
  /* Front: brand side */
  .card--front {
    left: 60px; top: 80px;
    background: var(--brand-blue);
    color: var(--card-white);
    display: flex; flex-direction: column;
    align-items: center; justify-content: center;
  }
  .brand-name {
    font-size: 104px; font-weight: 400; line-height: 1;
    letter-spacing: 10px; font-variant: normal;
  }
  .brand-tagline {
    margin-top: 18px; font-size: 21px; letter-spacing: 1.5px;
  }
  /* Back: contact side */
  .card--back {
    left: 600px; top: 480px;
    background: var(--card-white);
  }
  .person {
    position: absolute; left: 210px; top: 34px; width: 260px;
    text-align: center; color: var(--brand-blue);
  }
  .person__name { font-size: 25px; letter-spacing: .5px; line-height: 1.1; }
  .person__title {
    display: flex; align-items: center; gap: 8px;
    color: var(--ink); font-size: 14px; letter-spacing: 1px;
  }
  .person__title::before, .person__title::after {
    content: ""; flex: 1; height: 1px; background: var(--brand-blue);
  }
  .logo-block {
    position: absolute; left: 40px; top: 125px;
    width: 200px; height: 110px;
    background: var(--brand-blue); color: var(--card-white);
    display: flex; flex-direction: column; align-items: center; justify-content: center;
  }
  .logo-block .brand-name { font-size: 46px; letter-spacing: 5px; }
  .logo-block .brand-tagline { margin-top: 8px; font-size: 10.5px; letter-spacing: .6px; }
  .divider {
    position: absolute; left: 260px; top: 108px;
    width: 1px; height: 118px; background: var(--ink);
  }
  .contact {
    position: absolute; left: 276px; top: 104px;
    list-style: none; color: var(--ink);
    font-size: 14.5px; line-height: 21px;
  }
  .contact li { display: flex; align-items: center; gap: 7px; }
  .contact svg { width: 12px; height: 12px; fill: var(--brand-blue); flex: none; }
  .offices {
    position: absolute; left: 0; right: 0; bottom: 26px;
    text-align: center; color: var(--brand-blue);
    font-size: 17px; letter-spacing: .5px; word-spacing: 2px;
  }
  .offices .sep { color: var(--ink); margin: 0 6px; }
</style>
</head>
<body>
  <section class="card card--front" aria-label="Card front">
    <div class="brand-name">KMR</div>
    <div class="brand-tagline">Personal Injury Attorneys</div>
  </section>

  <section class="card card--back" aria-label="Card back">
    <div class="person">
      <div class="person__name">Tobin Verulakis</div>
      <div class="person__title">Attorney</div>
    </div>

    <div class="logo-block">
      <div class="brand-name">KMR</div>
      <div class="brand-tagline">Personal Injury Attorneys</div>
    </div>

    <div class="divider"></div>

    <ul class="contact">
      <li>812 W. Holloway Ave. 4th Floor</li>
      <li>Larkhaven, CA 90412</li>
      <li>
        <svg viewBox="0 0 12 12" aria-hidden="true"><path d="M3 0h6a1 1 0 0 1 1 1v10a1 1 0 0 1-1 1H3a1 1 0 0 1-1-1V1a1 1 0 0 1 1-1zm0 1.5v8h6v-8z"/></svg>
        (555)471-6029
      </li>
      <li>
        <svg viewBox="0 0 12 12" aria-hidden="true"><path d="M2.5 1 4.5 3 3.5 4.5c.8 1.6 2 2.8 3.5 3.5L8.5 7 11 9l-1.2 2C5.5 11 1 6.5 1 2.2z"/></svg>
        (555)963-1157
      </li>
      <li>
        <svg viewBox="0 0 12 12" aria-hidden="true"><path d="M0 2h12v8H0zm1 1 5 3.5L11 3z"/></svg>
        Tobin@counselwestmail.example
      </li>
    </ul>

    <div class="offices">Port Alder<span class="sep">|</span>Cedar Vale<span class="sep">|</span>Marisol Bay<span class="sep">|</span>North Hollis</div>
  </section>
</body>
</html>
```